Marlow Institute Flyer Design Project

we need a flyer which promotes our business products and services, our image.

must have list of all our courses, please view our website for further information.

www.marlowinstitute.net.au

Industry/Entity Type

Business

```html
<!DOCTYPE html>
<html lang="en">
<head>
<meta charset="utf-8">
<title>Marlow Institute – A Bright Future</title>
<link rel="stylesheet" href="https://fonts.googleapis.com/css2?family=Ubuntu:wght@400;500;700&family=Roboto:wght@300;400&display=swap">
<style>
  :root {
    --frame: #e4e4e4;
    --paper: #ffffff;
    --cyan-band: #00f6ff;
    --card: #44ddf8;
    --ink: #ffffff;
    --navy: #1c2f8a;
    --stripe-blue: #1b40d2;
    --stripe-orange: #f46a1c;
    --stripe-cream: #f8f3c2;
    --stripe-red: #c0130f;
  }
  * { box-sizing: border-box; margin: 0; padding: 0; }
  html, body { width: 1200px; height: 857px; overflow: hidden; background: var(--frame); }
  .flyer {
    position: relative; width: 1200px; height: 857px; background: var(--frame);
    font-family: "Ubuntu", sans-serif; color: var(--ink);
  }
  .sheet { position: absolute; left: 15px; top: 14px; width: 1170px; height: 828px; background: var(--paper); }
  .header { position: absolute; left: 15px; top: 14px; width: 1170px; height: 106px; background: var(--cyan-band); }
  .brand {
    position: absolute; left: 68px; top: 14px; width: 123px; height: 76px;
    background: var(--paper); border: 2px solid var(--navy);
    display: flex; flex-direction: column; align-items: center; justify-content: center; gap: 8px;
  }
  .brand-mark { width: 26px; height: 26px; background: var(--navy); }
  .brand-name { font-weight: 700; font-size: 11px; color: var(--navy); letter-spacing: .2px; }
  .tagline { position: absolute; right: 653px; top: 30px; text-align: right; white-space: nowrap; }
  .tagline h1 { font-size: 22.5px; font-weight: 700; line-height: 1; }
  .tagline p { font-family: "Roboto", sans-serif; font-weight: 300; font-size: 15px; margin-top: 2px; }
  .contact {
    position: absolute; right: 68px; top: 18px; text-align: right;
    font-family: "Roboto", sans-serif; font-weight: 300; font-size: 13px; line-height: 14px;
  }
  .contact .web { margin-top: 14px; }
  .course {
    position: absolute; width: 450px; height: 148px; background: var(--card);
    padding: 18px 31px 0 26px; border-bottom: 6px solid var(--stripe);
  }
  .course h2 { font-size: 16px; font-weight: 500; line-height: 18px; }
  .course h3 { font-size: 9px; font-weight: 700; line-height: 10px; margin-top: 1px; }
  .course p { font-size: 7.3px; line-height: 8.4px; letter-spacing: .45px; margin-top: 12px; }
  .course h3 + p { margin-top: 2px; }
  .course .code { font-size: 6.9px; line-height: 9px; letter-spacing: .2px; text-align: right; margin-top: 1px; }
  .col-left { left: 83px; } .col-right { left: 667px; }
  .row-1 { top: 142px; } .row-2 { top: 314px; } .row-3 { top: 485px; } .row-4 { top: 657px; }
  .stripe-blue { --stripe: var(--stripe-blue); }
  .stripe-orange { --stripe: var(--stripe-orange); }
  .stripe-cream { --stripe: var(--stripe-cream); }
  .stripe-red { --stripe: var(--stripe-red); }
  .campus-photo {
    position: absolute; left: 600px; top: 657px; width: 585px; height: 164px;
    background: linear-gradient(100deg, #7a5a3c 0%, #b89877 30%, #6f6a66 55%, #c7a782 80%, #e8c79e 100%);
  }
  .footer { position: absolute; left: 15px; top: 821px; width: 1170px; height: 21px; background: var(--cyan-band); }
</style>
</head>
<body>
<div class="flyer">
  <div class="sheet"></div>

  <header class="header">
    <div class="brand">
      <span class="brand-mark"></span>
      <span class="brand-name">MARLOW INSTITUTE</span>
    </div>
    <div class="tagline">
      <h1>A Bright Future</h1>
      <p>We get you ready</p>
    </div>
    <div class="contact">
      <div>Enquiries us today!</div>
      <div>+617 3000 4821</div>
      <div>enquiries@marlowinstitute.net.au</div>
      <div class="web">www.marlowinstitute.net.au</div>
    </div>
  </header>

  <section class="course col-left row-1 stripe-blue">
    <h2>Certificate IV in Business</h2>
    <p>Lorem ipsum dolor sit amet, consectetur adipiscing elit. Pellentesque vitae eros at sem placerat hendrerit at a neque. Donec ac libero quis eros aliquet sollicitudin nec ac metus. Maecenas tellus tellus, tempor id bibendum ut, scelerisque lacinia justo. Suspendisse libero purus, egestas id vehicula at, lacinia sit amet turpis. Proin pellentesque libero ac leo vehicula bibendum. Vivamus placerat tincidunt vulputate. Phasellus luctus, eros ut porttitor sagittis, orci metus vehicula felis, at posuere lectus sem eu ante. Aliquam pellentesque quam ut sem aliquam nec consectetur nisl porttitor. Morbi suscipit gravida lorem quis blandit. Vivamus in imperdiet erat. Aenean id est eget neque mattis ornare. Fusce lacinia mauris vitae ante rutrum ultricies. Donec porta pharetra diam eu bibendum. Aliquam erat volutpat. Mauris quis urna lacus.</p>
    <div class="code">MIB40110 CRICOS CODE: 095120A</div>
  </section>

  <section class="course col-right row-1 stripe-blue">
    <h2>Certificate III in Hospitality(Patisserie)</h2>
    <p>Lorem ipsum dolor sit amet, consectetur adipiscing elit. Pellentesque vitae eros at sem placerat hendrerit at a neque. Donec ac libero quis eros aliquet sollicitudin nec ac metus. Maecenas tellus tellus, tempor id bibendum ut, scelerisque lacinia justo. Suspendisse libero purus, egestas id vehicula at, lacinia sit amet turpis. Proin pellentesque libero ac leo vehicula bibendum. Vivamus placerat tincidunt vulputate. Phasellus luctus, eros ut porttitor sagittis, orci metus vehicula felis, at posuere lectus sem eu ante. Aliquam pellentesque quam ut sem aliquam nec consectetur nisl porttitor. Morbi suscipit gravida lorem quis blandit. Vivamus in imperdiet erat. Aenean id est eget neque mattis ornare. Fusce lacinia mauris vitae ante rutrum ultricies. Donec porta pharetra diam eu bibendum. Aliquam erat volutpat. Mauris quis urna lacus.</p>
    <div class="code">MIH31120 CRICOS CODE:0951347D</div>
  </section>

  <section class="course col-left row-2 stripe-orange">
    <h2>Diploma of Management</h2>
    <p>Lorem ipsum dolor sit amet, consectetur adipiscing elit. Pellentesque vitae eros at sem placerat hendrerit at a neque. Donec ac libero quis eros aliquet sollicitudin nec ac metus. Maecenas tellus tellus, tempor id bibendum ut, scelerisque lacinia justo. Suspendisse libero purus, egestas id vehicula at, lacinia sit amet turpis. Proin pellentesque libero ac leo vehicula bibendum. Vivamus placerat tincidunt vulputate. Phasellus luctus, eros ut porttitor sagittis, orci metus vehicula felis, at posuere lectus sem eu ante. Aliquam pellentesque quam ut sem aliquam nec consectetur nisl porttitor. Morbi suscipit gravida lorem quis blandit. Vivamus in imperdiet erat. Aenean id est eget neque mattis ornare. Fusce lacinia mauris vitae ante rutrum ultricies. Donec porta pharetra diam eu bibendum. Aliquam erat volutpat. Mauris quis urna lacus.</p>
    <div class="code">MIB51130 CRICOS CODE:095162E</div>
  </section>

  <section class="course col-right row-2 stripe-orange">
    <h2>Certificate IV in Hospitality</h2>
    <h3>(Commercial Cookery)</h3>
    <p>Lorem ipsum dolor sit amet, consectetur adipiscing elit. Pellentesque vitae eros at sem placerat hendrerit at a neque. Donec ac libero quis eros aliquet sollicitudin nec ac metus. Maecenas tellus tellus, tempor id bibendum ut, scelerisque lacinia justo. Suspendisse libero purus, egestas id vehicula at, lacinia sit amet turpis. Proin pellentesque libero ac leo vehicula bibendum. Vivamus placerat tincidunt vulputate. Phasellus luctus, eros ut porttitor sagittis, orci metus vehicula felis, at posuere lectus sem eu ante. Aliquam pellentesque quam ut sem aliquam nec consectetur nisl porttitor. Morbi suscipit gravida lorem quis blandit. Vivamus in imperdiet erat. Aenean id est eget neque mattis ornare. Fusce lacinia mauris vitae ante rutrum ultricies. Donec porta pharetra diam eu bibendum. Aliquam erat volutpat. Mauris quis urna lacus.</p>
    <div class="code">MIH40140 CRICOS CODE:095178F</div>
  </section>

  <section class="course col-left row-3 stripe-cream">
    <h2>Advance Diploma of Management</h2>
    <p>Lorem ipsum dolor sit amet, consectetur adipiscing elit. Pellentesque vitae eros at sem placerat hendrerit at a neque. Donec ac libero quis eros aliquet sollicitudin nec ac metus. Maecenas tellus tellus, tempor id bibendum ut, scelerisque lacinia justo. Suspendisse libero purus, egestas id vehicula at, lacinia sit amet turpis. Proin pellentesque libero ac leo vehicula bibendum. Vivamus placerat tincidunt vulputate. Phasellus luctus, eros ut porttitor sagittis, orci metus vehicula felis, at posuere lectus sem eu ante. Aliquam pellentesque quam ut sem aliquam nec consectetur nisl porttitor. Morbi suscipit gravida lorem quis blandit. Vivamus in imperdiet erat. Aenean id est eget neque mattis ornare. Fusce lacinia mauris vitae ante rutrum ultricies. Donec porta pharetra diam eu bibendum. Aliquam erat volutpat. Mauris quis urna lacus.</p>
    <div class="code">MIB60150 CRICOS CODE: 095184H</div>
  </section>

  <section class="course col-right row-3 stripe-cream">
    <h2>Diploma of Hospitality</h2>
    <p>Lorem ipsum dolor sit amet, consectetur adipiscing elit. Pellentesque vitae eros at sem placerat hendrerit at a neque. Donec ac libero quis eros aliquet sollicitudin nec ac metus. Maecenas tellus tellus, tempor id bibendum ut, scelerisque lacinia justo. Suspendisse libero purus, egestas id vehicula at, lacinia sit amet turpis. Proin pellentesque libero ac leo vehicula bibendum. Vivamus placerat tincidunt vulputate. Phasellus luctus, eros ut porttitor sagittis, orci metus vehicula felis, at posuere lectus sem eu ante. Aliquam pellentesque quam ut sem aliquam nec consectetur nisl porttitor. Morbi suscipit gravida lorem quis blandit. Vivamus in imperdiet erat. Aenean id est eget neque mattis ornare. Fusce lacinia mauris vitae ante rutrum ultricies. Donec porta pharetra diam eu bibendum. Aliquam erat volutpat. Mauris quis urna lacus.</p>
    <div class="code">MIH50160 CRICOS CODE:095191K</div>
  </section>

  <section class="course col-left row-4 stripe-red">
    <h2>Certificate III in Hospitality</h2>
    <h3>(Commercial Cookery)</h3>
    <p>Lorem ipsum dolor sit amet, consectetur adipiscing elit. Pellentesque vitae eros at sem placerat hendrerit at a neque. Donec ac libero quis eros aliquet sollicitudin nec ac metus. Maecenas tellus tellus, tempor id bibendum ut, scelerisque lacinia justo. Suspendisse libero purus, egestas id vehicula at, lacinia sit amet turpis. Proin pellentesque libero ac leo vehicula bibendum. Vivamus placerat tincidunt vulputate. Phasellus luctus, eros ut porttitor sagittis, orci metus vehicula felis, at posuere lectus sem eu ante. Aliquam pellentesque quam ut sem aliquam nec consectetur nisl porttitor. Morbi suscipit gravida lorem quis blandit. Vivamus in imperdiet erat. Aenean id est eget neque mattis ornare. Fusce lacinia mauris vitae ante rutrum ultricies. Donec porta pharetra diam eu bibendum. Aliquam erat volutpat. Mauris quis urna lacus.</p>
    <div class="code">MIH30170 CRICOS CODE:095207M</div>
  </section>

  <div class="campus-photo" role="img" aria-label="Photo of smiling students in a lecture hall"></div>

  <footer class="footer"></footer>
</div>
</body>
</html>
```